Qel Programming Video Tutorial Blog

Please be aware I am flexible with budget, I will increase it for great design thanks

A blog (wordpress) design required for video blogging teaching Qel Programming (creating ravlet apps). There are 4 pages required to be designed, the landing page where user submit their name and email (also shows an intro video), the main video blogging page (with beautiful video placeholder), a normal text blog page with big image at the top of each post and finally the portfolio page. The portfolio is where the tutor showcase all his previous developed apps and other projects to show his expertise.

The colour combination preferred are a mixture of blue and orange but we are open to other beautiful color combinations. Minimalistic design with lots of white and clare objectives for each page. The design should reflect the purpose of the website, someone who cannot read english landing on the page should immediately realise the page is made for learning to design ravlet apps.

I like curves and round corners, especially comment and portfolio pages with curves etc thanks

The blog domain will be quibnest.com

Target Market(s)

new programmer on the ravlet platform

Industry/Entity Type

Learning

Requirements
Must have
• ravlet image in the design
landing page has a video intro and Ravlet/mork image
Nice to have
• curves. round corners and circular shapes

```html
<!DOCTYPE html>
<html lang="en">
<head>
<meta charset="utf-8">
<title>Quibnest – Learn Qel Programming</title>
<link rel="stylesheet" href="https://fonts.googleapis.com/css2?family=Arimo:wght@400;700&family=Ropa+Sans&display=swap">
<style>
:root{
  --orange:#e07b14;
  --orange-light:#f6a623;
  --blue:#1a6fb0;
  --sky-top:#55bce6;
  --sky-bottom:#a9ddf4;
  --text:#555;
  --dark:#333;
  --line:#ddd;
  --panel:#f6f6f6;
}
*{margin:0;padding:0;box-sizing:border-box}
html,body{width:952px;height:1200px;overflow:hidden;background:#fff}
body{position:relative;font-family:"Arimo",Arial,sans-serif;color:var(--text)}
.abs{position:absolute}

/* header */
.site-header{left:0;top:0;width:952px;height:83px;background:linear-gradient(#fff,#f3f3f3);border-bottom:1px solid #e6e6e6}
.brand{left:73px;top:18px;display:flex;align-items:center;gap:8px}
.brand-mark{width:36px;height:36px;border-radius:50%;background:var(--blue)}
.brand-name{font-family:"Ropa Sans",sans-serif;font-size:32px;color:var(--blue);line-height:1}
.main-nav{right:72px;top:36px;display:flex;font-size:11px;font-weight:700}
.main-nav a{text-decoration:none;padding:0 15px;border-left:1px solid #d4d4d4;color:var(--blue)}
.main-nav a:first-child{border-left:0;color:var(--dark)}
.main-nav a.accent{color:var(--orange)}
.main-nav a:last-child{padding-right:0}

/* hero */
.hero{left:0;top:83px;width:952px;height:339px;background:linear-gradient(var(--sky-top),var(--sky-bottom));overflow:hidden}
.hero-media{left:73px;top:38px;width:565px;height:288px;border-radius:8px;background:linear-gradient(120deg,#4a4540,#7a8a9a 55%,#5f88b8)}
.hero-video-title{left:0;top:28px;width:355px;text-align:center;color:#fff;font-weight:700;font-size:29px;text-shadow:0 1px 3px rgba(0,0,0,.5)}
.hero-play{left:154px;top:88px}
.hero-tagline{right:71px;top:70px;font-family:"Ropa Sans",sans-serif;font-size:26px;color:#fff;white-space:nowrap}
.hero-title{right:71px;top:105px;font-size:34px;font-weight:700;color:#fff;text-shadow:0 1px 4px rgba(0,60,110,.35)}
.store-badge{top:149px;height:35px;border-radius:4px;background:#111;border:1px solid #666}
.slider-dots{left:819px;top:314px;display:flex;gap:6px}
.slider-dots span{width:11px;height:11px;border-radius:50%;background:#9ba6ab;border:1px solid #777}
.slider-dots span:first-child{background:#333}

/* welcome */
.section-title{font-family:"Ropa Sans",sans-serif;font-weight:400;color:var(--orange);font-size:21px;line-height:1}
.welcome-title{left:0;top:441px;width:952px;text-align:center;font-size:25px}
.welcome-text{left:102px;top:479px;width:760px;font-size:11.6px;line-height:20px}
.divider{left:72px;width:810px;height:1px;background:var(--line)}

/* signup */
.signup-title{left:79px;top:604px}
.signup-panel{left:76px;top:635px;width:265px;height:267px;background:var(--panel);border:1px solid #e2e2e2;border-radius:4px}
.field{left:17px;width:232px;height:33px;background:linear-gradient(#fff 80%,#ececec);border:1px solid #dcdcdc;border-radius:2px;padding:0 11px;font-size:11px;line-height:31px;color:#777}
.next-btn{left:174px;top:220px;width:75px;height:32px;border-radius:3px;background:linear-gradient(var(--orange-light),#ee8c0f);border:1px solid #d2790c;color:#333;font-size:15px;line-height:30px;text-align:center}
.column-rule{left:375px;top:604px;width:1px;height:298px;background:var(--line)}

/* blog */
.blog-title{left:401px;top:604px}
.post-thumb{left:402px;width:175px;height:102px;border:3px solid #ddd;border-radius:2px}
.post-text{left:590px;width:292px;font-size:11px;line-height:18.2px;text-align:justify}
.share-row{left:590px;display:flex;gap:6px;font-size:9px}
.share-row span{display:inline-flex;align-items:center;gap:3px;height:14px;padding:0 4px;border:1px solid #ccc;border-radius:2px;background:#f3f6fa;color:#3b5998}
.share-row .count{background:#fff;color:#555}
.share-row i{width:8px;height:8px;background:var(--blue);display:inline-block}
.pager{left:647px;top:880px;display:flex;gap:3px;font-size:9px;align-items:center}
.pager span{width:18px;height:18px;border-radius:2px;background:linear-gradient(#e2e2e2,#c9c9c9);color:#999;text-align:center;line-height:18px}
.pager span.current{background:linear-gradient(#888,#5e5e5e);color:#fff;font-weight:700}
.pager .gap{background:none;width:14px}

/* about */
.about-title{left:75px;top:960px}
.about-photo{left:76px;top:989px;width:174px;height:102px;border:3px solid #ddd;background:linear-gradient(120deg,#8b7355,#c8b89c 55%,#eee)}
.about-text{left:264px;top:995px;width:618px;font-size:11px;line-height:18.2px;text-align:justify}

/* footer */
.site-footer{left:0;top:1118px;width:952px;height:82px;background:linear-gradient(#383838,#262626);color:#ddd;font-size:11px;font-weight:700}
.footer-nav{left:73px;top:22px;display:flex}
.footer-nav a{color:#ddd;text-decoration:none}
.footer-nav em{font-style:normal;margin:0 9px}
.copyright{left:73px;top:49px;word-spacing:2px}
.social{top:27px;width:27px;height:27px;border-radius:4px;background:linear-gradient(#fff,#d8d8d8)}
</style>
</head>
<body>

<header class="site-header abs">
  <div class="brand abs"><span class="brand-mark"></span><span class="brand-name">Quibnest</span></div>
  <nav class="main-nav abs">
    <a href="#">About us</a><a href="#">Services</a><a href="#">Aplications</a><a href="#">Support</a><a href="#" class="accent">Register</a><a href="#" class="accent">Login</a>
  </nav>
</header>

<section class="hero abs">
  <div class="hero-media abs" role="img" aria-label="Desktop monitor, tablet and phone each playing the intro video">
    <div class="hero-video-title abs">How it works</div>
    <svg class="hero-play abs" width="48" height="48" viewBox="0 0 48 48"><circle cx="24" cy="24" r="23" fill="#eee" stroke="#bbb"/><path d="M18 13 L36 24 L18 35 Z" fill="#888"/></svg>
  </div>
  <div class="hero-tagline abs">Nam massa nisi, tincidunt amet accumsan</div>
  <div class="hero-title abs">MORBI IDPURUS</div>
  <div class="store-badge abs" style="left:659px;width:106px"></div>
  <div class="store-badge abs" style="left:772px;width:105px"></div>
  <div class="slider-dots abs"><span></span><span></span><span></span><span></span></div>
</section>

<h1 class="section-title welcome-title abs">Welcome to Quibnest</h1>
<p class="welcome-text abs">Sed quis lectus at ante dapibus gravida. Nam lobortis vehicula turpis ut feugiat. Mauris sodales eleifend est, eget cursus ipsum venenatis venenatis. Sed nec laoreet neque. Aenean mollis tempor ipsum. Pellentesque habitant morbi tristique senectus et netus et malesuada fames ac turpis egestas. Vivamus semper interdum quam at aliquet. Mauris bibendum facilisis est, non porta dolor aliquet ut. Integer lobortis nibh eget condimentum tristique. Vestibulum ante ipsum primis in faucibus orci luctus et ultrices posuere cubilia Curae; Aliquam tempus felis vitae dapibus ultricies.</p>
<div class="divider abs" style="top:578px"></div>

<h2 class="section-title signup-title abs">Get your own website in seconds</h2>
<form class="signup-panel abs">
  <div class="field abs" style="top:20px">Name</div>
  <div class="field abs" style="top:70px">Email</div>
  <div class="field abs" style="top:121px">Password</div>
  <div class="field abs" style="top:171px">Confirm Password</div>
  <div class="next-btn abs">Next &raquo;</div>
</form>
<div class="column-rule abs"></div>

<h2 class="section-title blog-title abs">Our Blog</h2>
<div class="post-thumb abs" style="top:635px;background:radial-gradient(circle at 45% 60%,#c8904a,#3a2a1c 35%,#050505 70%)" role="img" aria-label="Hand holding a glowing light bulb"></div>
<p class="post-text abs" style="top:636px">Sed quis lectus at ante dapibus gravida. Nam lobortis vehicula turpis ut feugiat. Mauris sodales eleifend est, eget cursus ipsum venenatis venenatis. Sed nec laoreet neque. Aenean mollis tempor ipsum.</p>
<div class="share-row abs" style="top:717px"><span><i></i>Like</span><span class="count">3k</span><span><i></i>Share</span><span class="count">316</span></div>

<div class="post-thumb abs" style="top:758px;background:linear-gradient(135deg,#1e5a8e,#d09a5a 50%,#1b3c6a)" role="img" aria-label="Wall of video screens showing beach scenes"></div>
<p class="post-text abs" style="top:759px">Sed quis lectus at ante dapibus gravida. Nam lobortis vehicula turpis ut feugiat. Mauris sodales eleifend est, eget cursus ipsum venenatis venenatis. Sed nec laoreet neque. Aenean mollis tempor ipsum.</p>
<div class="share-row abs" style="top:840px"><span><i></i>Like</span><span class="count">3k</span><span><i></i>Share</span><span class="count">316</span></div>

<div class="pager abs"><span class="current">1</span><span>2</span><span>3</span><span>4</span><span>5</span><span>6</span><span>7</span><span>8</span><span>&raquo;</span><span class="gap">…</span><span>&raquo;&raquo;</span></div>

<div class="divider abs" style="top:935px"></div>

<h2 class="section-title about-title abs">About Developer</h2>
<div class="about-photo abs" role="img" aria-label="Developer at a laptop in a library"></div>
<p class="about-text abs">Aenean placerat sem nisl, ac cursus sapien tempus a. In lectus odio, facilisis ut justo id, tincidunt iaculis nibh. Praesent ut risus lectus. Quisque sit amet elit magna. Integer hendrerit eu justo at vestibulum. Donec felis orci, dignissim a sapien sit amet, fermentum facilisis sem. Nam sed mattis elit. Donec porta viverra elit sed iaculis. Praesent nec massa non tortor tempus tempus. Donec at dolor ut sapien bibendum pharetra a dapibus lacus. Etiam aliquam tortor id eleifend egestas. Nullam sagittis in est ac varius. Suspendisse eget vestibulum eros.</p>

<footer class="site-footer abs">
  <nav class="footer-nav abs"><a href="#">Home</a><em>|</em><a href="#">About us</a><em>|</em><a href="#">Services</a><em>|</em><a href="#">Aplications</a><em>|</em><a href="#">Support</a><em>|</em><a href="#">Register</a><em>|</em><a href="#">Login</a></nav>
  <div class="copyright abs">Copyright &copy; 2013 &nbsp; quibnest.com &nbsp; All rights reserved.</div>
  <div class="social abs" style="left:696px"></div>
  <div class="social abs" style="left:736px"></div>
  <div class="social abs" style="left:776px"></div>
  <div class="social abs" style="left:816px"></div>
  <div class="social abs" style="left:855px"></div>
</footer>

</body>
</html>
```